Lyrebell Wedding Bombonieries

Wedding Bomboniere

these are for wedding favors I have a logo and a pic that I would like to add not sure how to send through to you also card shouls be a wedding theme

Target Market(s)

brides

Industry/Entity Type

Wedding

Contact Information for Business Card

Marguerite Oslowski
0432 591 604
email dorvin@plumtelnet.com.au
www.lyrebell.com.au

```html
<!DOCTYPE html>
<html lang="en">
<head>
<meta charset="utf-8">
<title>Lyrebell Wedding Bombonieries</title>
<link rel="stylesheet" href="https://fonts.googleapis.com/css2?family=Squada+One&display=swap">
<style>
  :root {
    --lime: #5cff0f;
    --red: #ff1020;
    --white: #ffffff;
    --frame-shadow: #b9b9b9;
    --photo-dark: #4a4f58;
    --photo-pink: #e0467a;
  }
  html, body {
    margin: 0;
    padding: 0;
    overflow: hidden;
    background: var(--white);
  }
  .card {
    position: relative;
    width: 1200px;
    height: 693px;
    overflow: hidden;
    background: var(--white);
    font-family: "Squada One", sans-serif;
  }
  .band-top, .band-bottom {
    position: absolute;
    left: 0;
    width: 1200px;
    background: var(--lime);
  }
  .band-top { top: 0; height: 66px; }
  .band-bottom { top: 622px; height: 71px; }
  .title-band {
    position: absolute;
    left: 0;
    top: 75px;
    width: 1200px;
    height: 216px;
    background: linear-gradient(to right, var(--white) 0px, var(--red) 470px, var(--red) 100%);
  }
  .title {
    position: absolute;
    left: 440px;
    top: 108px;
    width: 700px;
    margin: 0;
    text-align: center;
    color: var(--white);
    font-weight: 400;
    font-size: 78px;
    line-height: 80px;
    letter-spacing: 1px;
  }
  .photo-frame {
    position: absolute;
    left: 77px;
    top: 183px;
    width: 380px;
    height: 305px;
    background: var(--white);
    box-shadow: 4px 6px 6px var(--frame-shadow);
  }
  .photo-border {
    position: absolute;
    left: 13px;
    top: 15px;
    width: 356px;
    height: 274px;
    background: var(--lime);
  }
  .photo {
    position: absolute;
    left: 9px;
    top: 11px;
    width: 338px;
    height: 251px;
    background: radial-gradient(ellipse at 55% 40%, var(--photo-pink) 0%, #c9a0b4 30%, var(--photo-dark) 75%);
  }
  .contact {
    position: absolute;
    right: 294px;
    top: 330px;
    text-align: right;
    color: var(--red);
    line-height: 1;
  }
  .contact-name { font-size: 54px; margin: 0 0 30px; }
  .contact-phone { font-size: 46px; margin: 0 0 8px; letter-spacing: 1px; }
  .contact-line { font-size: 32px; margin: 0 0 8px; }
  .brand-mark {
    position: absolute;
    left: 952px;
    top: 338px;
    width: 194px;
    height: 194px;
    border-radius: 50%;
    background: var(--lime);
    display: flex;
    align-items: center;
    justify-content: center;
    color: var(--white);
    font-size: 44px;
  }
</style>
</head>
<body>
<div class="card">
  <div class="band-top"></div>
  <div class="title-band"></div>
  <h1 class="title">Lyrebell Wedding<br>Bombonieries</h1>

  <div class="photo-frame">
    <div class="photo-border">
      <div class="photo" role="img" aria-label="Photo of a glass jar wedding favour with a pink gingham fabric lid tied with twine"></div>
    </div>
  </div>

  <div class="contact">
    <p class="contact-name">Marguerite Oslowski</p>
    <p class="contact-phone">0432 591 604</p>
    <p class="contact-line">dorvin@plumtelnet.com.au</p>
    <p class="contact-line">www.lyrebell.com.au</p>
  </div>

  <div class="brand-mark">Lyrebell</div>

  <div class="band-bottom"></div>
</div>
</body>
</html>
```